I would like a business card to match my truck wrap and logo. I would like the font to match my existing business card please.

Industry/Entity Type

Painter

Contact Information for Business Card

Rodrigo Venaza 801-437-2916 Venazacoatings.utah@brushmail.net
SERVICES - Custom Paint & Stain, Interior & Exterior, Epoxy Coatings / Garage Floors, Cabinet Refinishing, Log Staining and Refinishing.

Requirements
Nice to have
• I would like to have the white and grey line like the bottom of my vehicle wrap, Light Grey to match my truck also.

```html
<!DOCTYPE html>
<html lang="en">
<head>
<meta charset="UTF-8">
<title>Venaza Coatings – Business Card</title>
<link href="https://fonts.googleapis.com/css2?family=Montserrat:wght@500;700;800&display=swap" rel="stylesheet">
<style>
  :root {
    --backdrop: #2a2b2d;
    --brand-blue: #1f7cc4;
    --blue-light: #2a9ede;
    --blue-deep: #1768ab;
    --card-white: #ffffff;
    --band-grey: #a3a7b3;
    --text-grey: #8d9099;
    --dot-blue: #2a98dc;
  }
  * { margin: 0; padding: 0; box-sizing: border-box; }
  html, body {
    width: 1200px; height: 900px; overflow: hidden;
    background: var(--backdrop);
    font-family: "Montserrat", Arial, sans-serif;
  }
  .canvas { position: relative; width: 1200px; height: 900px; }

  .card {
    position: absolute;
    width: 720px; height: 410px;
    border-radius: 24px;
    overflow: hidden;
  }

  /* Front */
  .card-front {
    left: 60px; top: 30px;
    background: linear-gradient(160deg, var(--blue-deep) 0%, var(--brand-blue) 45%, var(--blue-light) 100%);
  }
  .front-brand {
    position: absolute; inset: 0;
    display: flex; align-items: center; justify-content: center; gap: 22px;
  }
  .brand-square {
    flex: none;
    width: 64px; height: 64px; background: var(--card-white); border-radius: 6px;
  }
  .front-brand .brand-name {
    color: var(--card-white);
    font-weight: 800; font-size: 52px; letter-spacing: 2px; line-height: 1;
  }

  /* Back */
  .card-back {
    left: 420px; top: 470px;
    background: var(--card-white);
  }
  .band { position: absolute; left: 0; top: 0; width: 720px; height: 410px; }
  .owner-name {
    position: absolute; left: 36px; top: 34px;
    color: var(--brand-blue); font-weight: 700; font-size: 24px; letter-spacing: 1px;
  }
  .services-block {
    position: absolute; right: 34px; top: 28px;
    text-align: right;
  }
  .services-title {
    color: var(--brand-blue); font-weight: 800; font-size: 26px; letter-spacing: 1px;
    line-height: 1.2; margin-bottom: 6px; padding-right: 19px;
  }
  .services { list-style: none; }
  .services li {
    color: var(--text-grey); font-weight: 500; font-size: 15.5px; line-height: 24px;
    display: flex; justify-content: flex-end; align-items: center; gap: 10px;
  }
  .services li::after {
    content: ""; width: 9px; height: 9px; border-radius: 50%; background: var(--dot-blue);
  }
  .back-brand {
    position: absolute; left: 40px; top: 176px;
    display: flex; align-items: center; gap: 14px;
  }
  .back-brand .brand-square { width: 40px; height: 40px; background: var(--brand-blue); }
  .back-brand .brand-name {
    color: var(--brand-blue); font-weight: 800; font-size: 27px; letter-spacing: 1px; line-height: 1;
  }
  .contact {
    position: absolute; right: 30px; top: 268px;
    list-style: none; text-align: right;
  }
  .contact li {
    color: var(--card-white); font-weight: 500; font-size: 14px; line-height: 28px;
    display: flex; justify-content: flex-end; align-items: center; gap: 10px;
  }
  .contact svg { width: 16px; height: 16px; flex: none; }
</style>
</head>
<body>
<div class="canvas">

  <section class="card card-front">
    <div class="front-brand">
      <span class="brand-square"></span>
      <span class="brand-name">VENAZA COATINGS</span>
    </div>
  </section>

  <section class="card card-back">
    <svg class="band" viewBox="0 0 720 410" aria-hidden="true">
      <polygon points="0,345 330,345 392,222 720,222 720,410 0,410" fill="var(--band-grey)"/>
      <polyline points="0,362 342,362 404,240 720,240" fill="none" stroke="var(--card-white)" stroke-width="4"/>
    </svg>

    <h2 class="owner-name">RODRIGO VENAZA</h2>

    <div class="services-block">
      <h3 class="services-title">SERVICES</h3>
      <ul class="services">
        <li>Custom Paint &amp; Stain</li>
        <li>Interior &amp; Exterior</li>
        <li>Epoxy Coatings / Garage Floors</li>
        <li>Cabinet Refinishing</li>
        <li>Log Staining and Refinishing</li>
      </ul>
    </div>

    <div class="back-brand">
      <span class="brand-square"></span>
      <span class="brand-name">VENAZA COATINGS</span>
    </div>

    <ul class="contact">
      <li>801-437-2916
        <svg viewBox="0 0 24 24" fill="none" stroke="currentColor" stroke-width="2"><path d="M5 3h4l2 5-2.5 1.5a11 11 0 0 0 6 6L16 13l5 2v4a2 2 0 0 1-2 2A16 16 0 0 1 3 5a2 2 0 0 1 2-2z"/></svg>
      </li>
      <li>Venazacoatings.utah@brushmail.net
        <svg viewBox="0 0 24 24" fill="none" stroke="currentColor" stroke-width="2"><rect x="3" y="5" width="18" height="14" rx="1"/><path d="M3 6l9 7 9-7"/></svg>
      </li>
    </ul>
  </section>

</div>
</body>
</html>
```